Tri-Fold Brochure for Transportation Equipment Dealer

We need a design of a new tri-fold brochure for our company. This is what we give to customers and prospective customers. Many of our customers do not know the diversity of our product line and capabilities. We have a lot of information to share with them in a small package. I have provided a draft of the content that I wanted included (in a .pptx and .pdf format), but we need it enhanced with color and made to look more professional. We need it to be informative yet professional.

Target Market(s)

Transportation industry customers. Fleet carriers and owner/operator truck drivers.

Industry/Entity Type

Truck Service

Font styles to use
Serif
Sans Serif

Colors
3176b5

Requirements
Must have
• Color. Must include the information that I have provided in the draft. Must be US Letter size.
Nice to have
• Color and separation of different sections.

```html
<!DOCTYPE html>
<html lang="en">
<head>
<meta charset="utf-8">
<title>Eastline Bulk Supply – Tri-Fold Brochure</title>
<link href="https://fonts.googleapis.com/css2?family=Open+Sans:ital,wght@0,400;0,600;0,700;0,800;1,600&family=Merriweather:wght@700&display=swap" rel="stylesheet">
<style>
  :root{
    --blue:#3176b5;
    --navy:#1c2d6e;
    --deep:#101c4c;
    --sky:#5f9bd3;
    --paper:#ffffff;
    --mist:#eef1f5;
    --ink:#2b2f3a;
    --stage:#e4e5e7;
    --grass:#6b7f3c;
    --steel:#b9c1cc;
  }
  *{box-sizing:border-box;margin:0;padding:0}
  html,body{width:1200px;height:2400px;overflow:hidden;background:var(--stage);font-family:"Open Sans",Arial,sans-serif;color:var(--ink)}
  .spread{position:absolute;left:50px;width:1100px;height:850px;display:flex;background:var(--paper);box-shadow:0 6px 24px rgba(0,0,0,.18)}
  .spread--outside{top:280px}
  .spread--inside{top:1270px}
  .panel{position:relative;width:366.67px;height:100%;overflow:hidden;display:flex;flex-direction:column}
  .panel + .panel{border-left:1px solid rgba(0,0,0,.06)}
  .panel--navy{background:linear-gradient(180deg,var(--navy),var(--deep));color:#fff}
  .panel--mist{background:var(--mist)}
  .photo{display:block;border-radius:4px}
  .band{position:absolute;left:0;right:0;bottom:0;height:46px;background:var(--blue);color:#fff;display:flex;align-items:center;justify-content:center;gap:10px;font-weight:800;font-size:22px;letter-spacing:.5px}
  .band--web{font-size:16px;font-weight:700;background:var(--blue)}
  .band svg{width:22px;height:22px}
  .pill{display:inline-block;background:var(--navy);color:#fff;font-weight:800;font-size:15px;letter-spacing:1px;padding:5px 26px;border-radius:20px;text-transform:uppercase}
  .pill--blue{background:var(--blue)}
  .swoosh{position:absolute;left:0;top:0;width:100%;pointer-events:none;z-index:0}

  /* cover */
  .cover-head{position:relative;height:150px;padding:26px 24px 0}
  .cover-head .swoosh{top:auto;bottom:0}
  .brand{display:flex;align-items:center;gap:12px;position:relative;z-index:2}
  .brand-dot{width:46px;height:46px;border-radius:50%;background:var(--blue);flex:none}
  .brand-name{font-weight:800;color:var(--navy);font-size:13px;line-height:1.35;text-transform:uppercase;letter-spacing:.3px}
  .cover-photo{height:250px;margin:0;background:linear-gradient(180deg,#6fa6dd 0%,#9cc4ea 45%,#c9ced4 55%,#8d939b 68%,var(--grass) 80%,#4f6230 100%);border-radius:0}
  .products{display:grid;grid-template-columns:1fr 1fr;gap:10px 16px;padding:18px 26px 0}
  .product{text-align:center;font-size:10px;font-weight:600;color:var(--navy)}
  .product .photo{height:70px;background:linear-gradient(135deg,#f3f5f8,var(--steel));margin-bottom:3px}
  .tagline{padding:16px 24px 0;text-align:center}
  .tagline h1{font-family:"Merriweather",Georgia,serif;font-size:19px;line-height:1.25;color:var(--blue);text-transform:uppercase}
  .tagline p{margin-top:8px;font-weight:800;font-size:15px;color:var(--navy);letter-spacing:1px}

  /* services */
  .services{position:relative;z-index:1;padding:72px 22px 60px}
  .service{display:flex;align-items:center;gap:14px;margin-top:20px}
  .service p{font-size:12px;line-height:1.5;font-style:italic;font-weight:600;color:var(--ink);flex:1}
  .service .photo{width:110px;height:110px;border-radius:50%;flex:none;background:radial-gradient(circle at 40% 35%,#e9c14a,#4a4a4a 75%)}
  .service:nth-child(3) .photo{background:radial-gradient(circle at 40% 40%,#f0f0f0,#8a8f97 80%)}
  .partner-word{font-weight:800;font-size:15px;font-style:normal;color:var(--deep);margin-top:4px}
  .service-photos{display:flex;justify-content:space-between;margin-top:22px}
  .service-photos figure{text-align:center;font-size:10px;font-style:italic;color:var(--ink)}
  .service-photos .photo{width:72px;height:72px;border-radius:50%;background:radial-gradient(circle,#d9dde2,#7c828b);margin-bottom:4px}

  /* contact */
  .contact{padding:26px 22px 60px;text-align:center}
  .contact h2{font-size:15px;font-style:italic;font-weight:600;letter-spacing:.5px;text-transform:uppercase}
  .map{height:170px;margin:12px 10px 0;background:linear-gradient(90deg,#c9d2e6 0%,#d94848 30%,#ffffff 52%,#4a78c4 75%,#9db7e3 100%);border-radius:6px;opacity:.92}
  .hours{margin-top:14px;font-size:13px;line-height:1.45}
  .hours strong{display:block;font-size:14px;letter-spacing:.5px}
  .contact .pill{margin-top:10px;background:#fff;color:var(--navy)}
  .locations{display:grid;grid-template-columns:1fr 1fr;gap:14px 12px;margin-top:18px;text-align:left;font-size:10px;line-height:1.45}
  .locations b{display:block;color:var(--sky);font-size:10.5px;text-transform:uppercase}

  /* inside */
  .photo-strip{height:230px;flex:none;background:linear-gradient(180deg,#9aa5b3,#4c5563)}
  .panel--navy .photo-strip{background:linear-gradient(180deg,#aeb6c2,#5d6674)}
  .panel:nth-child(3) .photo-strip{background:linear-gradient(180deg,#b8a98c,#5a5f68)}
  .inner{padding:18px 24px 60px;position:relative}
  .inner .pill{display:table;margin:-34px auto 0;position:relative;z-index:2}
  .lead{text-align:center;font-weight:700;color:var(--navy);font-size:14px;margin-top:12px}
  .awards{display:flex;justify-content:space-around;margin-top:10px}
  .award{text-align:center;font-weight:800;font-size:12px;color:var(--navy)}
  .award svg{width:28px;height:30px;display:block;margin:0 auto 2px}
  .copy{font-size:11px;line-height:1.5;margin-top:12px}
  .checks{display:grid;grid-template-columns:1fr 1fr;gap:6px 10px;margin-top:12px;font-size:12px;font-weight:600}
  .checks li{list-style:none;display:flex;align-items:center;gap:6px}
  .checks svg{width:14px;height:14px;flex:none}
  .blower-row{display:flex;align-items:center;justify-content:space-between;margin-top:14px}
  .blower-row .photo{width:110px;height:56px;background:linear-gradient(135deg,#e0483f,#7c1d1a)}
  .panel--navy .copy{color:#e9eefb}
  .trailers{display:grid;grid-template-columns:1fr 1fr;gap:12px 14px;margin-top:14px}
  .trailer{font-size:10px;text-align:center;color:#dfe6f7}
  .trailer .photo{height:62px;background:linear-gradient(180deg,#f4f6f9,#9aa3b0);margin-bottom:3px}
  .badges{display:flex;justify-content:center;gap:12px;margin-top:14px}
  .badges span{width:78px;height:28px;border-radius:4px;background:#fff}
  .parts-intro{font-size:11px;text-align:center;margin-top:12px}
  .parts{display:grid;grid-template-columns:1fr 1fr;gap:12px 14px;margin-top:14px}
  .part{font-size:10.5px;text-align:center;font-weight:600;color:var(--navy)}
  .part .photo{height:54px;background:radial-gradient(circle,#9aa0aa,#3a3f48 80%);margin-bottom:3px}
</style>
</head>
<body>

<!-- OUTSIDE SPREAD -->
<section class="spread spread--outside">

  <article class="panel panel--mist services-panel">
    <svg class="swoosh" viewBox="0 0 367 60" height="60" preserveAspectRatio="none"><path d="M0 0H367V18C250 44 120 50 0 40Z" fill="var(--blue)"/></svg>
    <div class="services">
      <span class="pill pill--blue">Our Services</span>
      <div class="service-list">
        <div class="service">
          <p>All of our facilities provide mobile and shop service, installation and repair services.<span class="partner-word" style="display:block">Harlow Compressor</span></p>
          <div class="photo" role="img" aria-label="Photo of a service truck at a facility"></div>
        </div>
        <div class="service">
          <p>Including sandblasting, powder coating, custom fabrication and DOT service.</p>
          <div class="photo" role="img" aria-label="Photo of a yellow blower unit"></div>
        </div>
        <div class="service">
          <p>Blower service &amp; oil changes, vacuum pumps, liquid pumps, hydraulic systems, wet kits, hose and fittings, valves and accessories.</p>
          <div class="photo" role="img" aria-label="Photo of a tank trailer in the shop"></div>
        </div>
      </div>
      <div class="service-photos">
        <figure><div class="photo" role="img" aria-label="Photo of mobile service"></div>Mobile</figure>
        <figure><div class="photo" role="img" aria-label="Photo of blower work"></div>Blower</figure>
        <figure><div class="photo" role="img" aria-label="Photo of shop work"></div>Shop</figure>
        <figure><div class="photo" role="img" aria-label="Photo of parts"></div>Parts</figure>
      </div>
    </div>
    <div class="band"><svg viewBox="0 0 24 24"><circle cx="12" cy="12" r="11" fill="none" stroke="#fff" stroke-width="2"/><path d="M8 6l2.5 0 1 3-1.5 1.2a7 7 0 0 0 3.8 3.8L15 12.5l3 1v2.5c-5 .5-10.5-5-10-10z" fill="#fff"/></svg>800-555-0142</div>
  </article>

  <article class="panel panel--navy">
    <div class="contact">
      <h2>7 Locations to Serve You!</h2>
      <div class="map" role="img" aria-label="Map of the United States marking the seven locations"></div>
      <div class="hours"><strong>FACILITY HOURS</strong>Monday – Friday<br>8:00 AM – 5:00 PM</div>
      <span class="pill">Contact Us</span>
      <div class="locations">
        <div><b>Eastline – Tampa</b>4100 Harbor Rd<br>Tampa, FL 33610<br>Ph: 800-555-0142</div>
        <div><b>Westline – Tulsa</b>220 Prairie Ave<br>Tulsa, OK 74107<br>Ph: 800-555-0143</div>
        <div><b>Eastline – Macon</b>75 Depot Street<br>Macon, GA 31201<br>Ph: 800-555-0144</div>
        <div><b>Westline – Odessa</b>910 Mesa Drive<br>Odessa, TX 79761<br>Ph: 800-555-0145</div>
        <div><b>Bulkline Exports</b>18 Port Lane<br>Mobile, AL 36602<br>Ph: 800-555-0146</div>
        <div><b>Westline – Reno</b>3300 Valley Rd<br>Reno, NV 89502<br>Ph: 800-555-0147</div>
      </div>
    </div>
    <div class="band band--web">www.drybulkgear.com</div>
  </article>

  <article class="panel cover">
    <div class="cover-head">
      <svg class="swoosh" viewBox="0 0 367 56" height="56" preserveAspectRatio="none"><path d="M0 56V36C130 50 250 28 367 4V56Z" fill="var(--navy)"/><path d="M0 56V46C140 56 260 40 367 20V56Z" fill="var(--blue)"/></svg>
      <div class="brand">
        <span class="brand-dot"></span>
        <div class="brand-name">Eastline Bulk Supply<br>Westline Bulk Supply<br>Bulkline Exports</div>
      </div>
    </div>
    <div class="photo cover-photo" role="img" aria-label="Photo of a polished pneumatic tank trailer parked on grass under blue sky"></div>
    <div class="products">
      <div class="product"><div class="photo" role="img" aria-label="Photo of a bulk trailer"></div>Trailer</div>
      <div class="product"><div class="photo" role="img" aria-label="Photo of a blower unit"></div>Blower</div>
      <div class="product"><div class="photo" role="img" aria-label="Photo of a pneumatic tank"></div>Tank</div>
      <div class="product"><div class="photo" role="img" aria-label="Photo of a trailer-mounted pump"></div>Pump</div>
    </div>
    <div class="tagline">
      <h1>Experts in Dry Bulk Transportation Solutions</h1>
      <p>NEW · USED · SERVICES · PARTS</p>
    </div>
    <div class="band"><svg viewBox="0 0 24 24"><circle cx="12" cy="12" r="11" fill="none" stroke="#fff" stroke-width="2"/><path d="M8 6l2.5 0 1 3-1.5 1.2a7 7 0 0 0 3.8 3.8L15 12.5l3 1v2.5c-5 .5-10.5-5-10-10z" fill="#fff"/></svg>800-555-0142</div>
  </article>
</section>

<!-- INSIDE SPREAD -->
<section class="spread spread--inside">

  <article class="panel">
    <div class="photo-strip" role="img" aria-label="Photo of a technician servicing a blower in the shop"></div>
    <div class="inner">
      <span class="pill">Blowers</span>
      <p class="lead">#1 USA mobile blower distributor</p>
      <div class="awards">
        <div class="award"><svg viewBox="0 0 28 30"><path d="M7 2h14v8a7 7 0 0 1-14 0z M7 4H2c0 5 3 7 6 7 M21 4h5c0 5-3 7-6 7" fill="#e8b730" stroke="#e8b730" stroke-width="1.5"/><rect x="12" y="17" width="4" height="6" fill="#e8b730"/><rect x="8" y="23" width="12" height="4" fill="#c99520"/></svg>2014</div>
        <div class="award"><svg viewBox="0 0 28 30"><path d="M7 2h14v8a7 7 0 0 1-14 0z M7 4H2c0 5 3 7 6 7 M21 4h5c0 5-3 7-6 7" fill="#e8b730" stroke="#e8b730" stroke-width="1.5"/><rect x="12" y="17" width="4" height="6" fill="#e8b730"/><rect x="8" y="23" width="12" height="4" fill="#c99520"/></svg>2015</div>
        <div class="award"><svg viewBox="0 0 28 30"><path d="M7 2h14v8a7 7 0 0 1-14 0z M7 4H2c0 5 3 7 6 7 M21 4h5c0 5-3 7-6 7" fill="#e8b730" stroke="#e8b730" stroke-width="1.5"/><rect x="12" y="17" width="4" height="6" fill="#e8b730"/><rect x="8" y="23" width="12" height="4" fill="#c99520"/></svg>2016</div>
        <div class="award"><svg viewBox="0 0 28 30"><path d="M7 2h14v8a7 7 0 0 1-14 0z M7 4H2c0 5 3 7 6 7 M21 4h5c0 5-3 7-6 7" fill="#e8b730" stroke="#e8b730" stroke-width="1.5"/><rect x="12" y="17" width="4" height="6" fill="#e8b730"/><rect x="8" y="23" width="12" height="4" fill="#c99520"/></svg>2017</div>
      </div>
      <p class="copy">We are proud to represent the Harlow Compressor line of mobile products for use in dry bulk and hydraulic applications. Harlow blowers are the most efficient and productive blowers on the market.</p>
      <p class="copy">We specialize in blower installations for your trailer or truck. With our expertise and several mode designs we can meet any mounting arrangement or need.</p>
      <p class="copy">We can integrate your system with hydraulics to meet power take-off units (PTO).</p>
      <ul class="checks">
        <li><svg viewBox="0 0 14 14"><rect x=".5" y=".5" width="13" height="13" rx="2" fill="none" stroke="var(--blue)"/><path d="M3 7l3 3 5-6" fill="none" stroke="var(--blue)" stroke-width="2"/></svg>Stock</li>
        <li><svg viewBox="0 0 14 14"><rect x=".5" y=".5" width="13" height="13" rx="2" fill="none" stroke="var(--blue)"/><path d="M3 7l3 3 5-6" fill="none" stroke="var(--blue)" stroke-width="2"/></svg>Repair</li>
        <li><svg viewBox="0 0 14 14"><rect x=".5" y=".5" width="13" height="13" rx="2" fill="none" stroke="var(--blue)"/><path d="M3 7l3 3 5-6" fill="none" stroke="var(--blue)" stroke-width="2"/></svg>PTO Kits</li>
        <li><svg viewBox="0 0 14 14"><rect x=".5" y=".5" width="13" height="13" rx="2" fill="none" stroke="var(--blue)"/><path d="M3 7l3 3 5-6" fill="none" stroke="var(--blue)" stroke-width="2"/></svg>Package Units</li>
      </ul>
      <div class="blower-row">
        <span class="partner-word">Harlow Compressor</span>
        <div class="photo" role="img" aria-label="Photo of a red blower"></div>
      </div>
    </div>
    <div class="band"><svg viewBox="0 0 24 24"><circle cx="12" cy="12" r="11" fill="none" stroke="#fff" stroke-width="2"/><path d="M8 6l2.5 0 1 3-1.5 1.2a7 7 0 0 0 3.8 3.8L15 12.5l3 1v2.5c-5 .5-10.5-5-10-10z" fill="#fff"/></svg>800-555-0142</div>
  </article>

  <article class="panel panel--navy">
    <div class="photo-strip" role="img" aria-label="Photo of tank trailers inside a service bay"></div>
    <div class="inner">
      <span class="pill pill--blue">Trailers</span>
      <p class="copy">We can custom configure your trailer to meet your needs.</p>
      <p class="copy">We have durability to an after-factory modifications to your trailer specs.</p>
      <div class="trailers">
        <div class="trailer"><div class="photo" role="img" aria-label="Photo of a pneumatic tank trailer"></div>Pneumatic Tank</div>
        <div class="trailer"><div class="photo" role="img" aria-label="Photo of a flatbed trailer"></div>Flatbed</div>
        <div class="trailer"><div class="photo" role="img" aria-label="Photo of a dry bulk trailer"></div>Dry Bulk Pneumatic</div>
        <div class="trailer"><div class="photo" role="img" aria-label="Photo of a hopper trailer"></div>Hopper</div>
        <div class="trailer"><div class="photo" role="img" aria-label="Photo of an end dump trailer"></div>End Dump</div>
        <div class="trailer"><div class="photo" role="img" aria-label="Photo of a belt trailer"></div>Belt Trailer</div>
      </div>
      <div class="badges"><span></span><span></span><span></span></div>
    </div>
    <div class="band band--web">www.drybulkgear.com</div>
  </article>

  <article class="panel">
    <div class="photo-strip" role="img" aria-label="Photo of a parts warehouse with stocked shelving"></div>
    <div class="inner">
      <span class="pill">Parts</span>
      <p class="parts-intro">Lots of parts in stock, ship within 24 hours of most all orders.</p>
      <div class="parts">
        <div class="part"><div class="photo" role="img" aria-label="Photo of trailer parts"></div>Trailer Parts</div>
        <div class="part"><div class="photo" role="img" aria-label="Photo of filters and breakaways"></div>Filter &amp; Breakaway</div>
        <div class="part"><div class="photo" role="img" aria-label="Photo of hydraulic wet line kit"></div>Hydraulic &amp; Wet Line Kits</div>
        <div class="part"><div class="photo" role="img" aria-label="Photo of a PTO unit"></div>PTO</div>
        <div class="part"><div class="photo" role="img" aria-label="Photo of hoses and fittings"></div>Hose &amp; Fittings</div>
        <div class="part"><div class="photo" role="img" aria-label="Photo of valves and fittings"></div>Valves &amp; Fittings</div>
        <div class="part"><div class="photo" role="img" aria-label="Photo of gaskets"></div>Gaskets</div>
        <div class="part"><div class="photo" role="img" aria-label="Photo of a vacuum pump"></div>Vacuum Pump</div>
      </div>
    </div>
    <div class="band"><svg viewBox="0 0 24 24"><circle cx="12" cy="12" r="11" fill="none" stroke="#fff" stroke-width="2"/><path d="M8 6l2.5 0 1 3-1.5 1.2a7 7 0 0 0 3.8 3.8L15 12.5l3 1v2.5c-5 .5-10.5-5-10-10z" fill="#fff"/></svg>800-555-0142</div>
  </article>
</section>

</body>
</html>
```